New Company Business Card design

Looking for a corporate looking business card utilising my new logo design - the logo i would like embossed as one option and flat as another - simplistic but stylish - less is more - we are an import export business launching into the market - i would like a couple of options as main background - Grey or Black

```html
<!DOCTYPE html>
<html lang="en">
<head>
<meta charset="utf-8">
<title>Meridian Trade Partners – Business Card</title>
<link href="https://fonts.googleapis.com/css2?family=Lato:ital,wght@0,300;0,400;0,700;1,300&display=swap" rel="stylesheet">
<style>
  :root {
    --page: #f3f4f5;
    --card: #0f1114;
    --blue: #2a78e0;
    --white: #f2f4f7;
    --grey: #8b9098;
    --muted: #5d636b;
  }
  * { box-sizing: border-box; margin: 0; padding: 0; }
  html, body {
    width: 1200px; height: 1200px; overflow: hidden;
    background: var(--page);
    font-family: "Lato", sans-serif;
  }
  .canvas {
    width: 1200px; height: 1200px;
    display: flex; flex-direction: column; align-items: center; justify-content: center;
    gap: 70px;
  }
  .card {
    position: relative;
    width: 880px; height: 503px;
    background: var(--card);
    border-radius: 28px;
    box-shadow: 0 18px 40px rgba(0,0,0,0.18);
    overflow: hidden;
  }

  /* front */
  .brand {
    position: absolute; left: 70px; top: 0; bottom: 0; width: 360px;
    display: flex; align-items: center; gap: 16px;
  }
  .brand-dot {
    width: 22px; height: 22px; border-radius: 50%;
    background: var(--blue); flex: none;
  }
  .brand-name {
    color: var(--blue);
    font-weight: 700; font-size: 26px; letter-spacing: 0.14em;
    text-transform: uppercase; line-height: 1.3;
  }
  .divider {
    position: absolute; left: 440px; top: 70px;
    width: 2px; height: 363px;
    background: linear-gradient(to bottom, rgba(42,120,224,0), var(--blue) 50%, rgba(42,120,224,0));
    transform: rotate(14deg);
  }
  .contact {
    position: absolute; left: 500px; top: 95px; right: 40px;
    color: var(--white);
  }
  .person-name { font-size: 38px; font-weight: 300; letter-spacing: 0.01em; }
  .person-role { font-size: 18px; font-weight: 300; font-style: italic; color: var(--grey); margin-top: 4px; }
  .details { list-style: none; margin-top: 30px; }
  .details li {
    display: flex; align-items: flex-start; gap: 14px;
    font-size: 20px; line-height: 1.25; margin-bottom: 10px;
    white-space: nowrap;
  }
  .details svg { width: 18px; height: 18px; flex: none; margin-top: 3px; fill: var(--blue); }
  .details .address { font-size: 17px; margin-bottom: 18px; }
  .details .email { color: var(--muted); }
  .details .email svg { fill: var(--muted); }

  /* back */
  .card-back {
    display: flex; align-items: center; justify-content: center; gap: 18px;
  }
  .card-back .brand-name { font-size: 30px; }
</style>
</head>
<body>
<main class="canvas">

  <section class="card card-front">
    <div class="brand">
      <span class="brand-dot"></span>
      <span class="brand-name">Meridian Trade Partners</span>
    </div>
    <div class="divider"></div>
    <div class="contact">
      <h1 class="person-name">Daniel Reyes</h1>
      <p class="person-role">Director</p>
      <ul class="details">
        <li class="address">
          <svg viewBox="0 0 24 24"><path d="M12 2a7 7 0 0 0-7 7c0 5 7 13 7 13s7-8 7-13a7 7 0 0 0-7-7zm0 9.5A2.5 2.5 0 1 1 12 6.5a2.5 2.5 0 0 1 0 5z"/></svg>
          <span>48 Harbour Lane, Suite 5<br>Portview, 2041</span>
        </li>
        <li>
          <svg viewBox="0 0 24 24"><path d="M6.6 10.8a15 15 0 0 0 6.6 6.6l2.2-2.2a1 1 0 0 1 1-.25 11.4 11.4 0 0 0 3.6.57 1 1 0 0 1 1 1V20a1 1 0 0 1-1 1A17 17 0 0 1 3 4a1 1 0 0 1 1-1h3.5a1 1 0 0 1 1 1c0 1.25.2 2.45.57 3.6a1 1 0 0 1-.25 1z"/></svg>
          <span>555 210 4830</span>
        </li>
        <li>
          <svg viewBox="0 0 24 24"><path d="M7 1h10a2 2 0 0 1 2 2v18a2 2 0 0 1-2 2H7a2 2 0 0 1-2-2V3a2 2 0 0 1 2-2zm0 4v13h10V5z"/></svg>
          <span>555 318 7742</span>
        </li>
        <li>
          <svg viewBox="0 0 24 24"><path d="M6 2h9l3 3v5H6zM4 11h16a2 2 0 0 1 2 2v7H2v-7a2 2 0 0 1 2-2zm3 4v2h10v-2z"/></svg>
          <span>555 210 4831</span>
        </li>
        <li>
          <svg viewBox="0 0 24 24"><path d="M12 2a10 10 0 1 0 0 20 10 10 0 0 0 0-20zm6.9 6h-3a15 15 0 0 0-1.3-3.9A8 8 0 0 1 18.9 8zM12 4c.8 1.2 1.5 2.5 1.9 4h-3.8c.4-1.5 1.1-2.8 1.9-4zM4.3 14a8 8 0 0 1 0-4h3.4a16 16 0 0 0 0 4zm.8 2h3a15 15 0 0 0 1.3 3.9A8 8 0 0 1 5.1 16zm3-8h-3a8 8 0 0 1 4.3-3.9A15 15 0 0 0 8.1 8zM12 20c-.8-1.2-1.5-2.5-1.9-4h3.8c-.4 1.5-1.1 2.8-1.9 4zm2.3-6H9.7a14 14 0 0 1 0-4h4.6a14 14 0 0 1 0 4zm.3 5.9a15 15 0 0 0 1.3-3.9h3a8 8 0 0 1-4.3 3.9zm1.7-5.9a16 16 0 0 0 0-4h3.4a8 8 0 0 1 0 4z"/></svg>
          <span>meridiantrade.example</span>
        </li>
        <li class="email">
          <svg viewBox="0 0 24 24"><path d="M3 5h18a1 1 0 0 1 1 1v12a1 1 0 0 1-1 1H3a1 1 0 0 1-1-1V6a1 1 0 0 1 1-1zm9 7.5L4 7.3V17h16V7.3z"/></svg>
          <span>daniel@meridiantrade.example</span>
        </li>
      </ul>
    </div>
  </section>

  <section class="card card-back">
    <span class="brand-dot"></span>
    <span class="brand-name">Meridian Trade Partners</span>
  </section>

</main>
</body>
</html>
```